Brisk Lantern Estates, which offers a selection of prime properties (villas

A website that contains: Idea, benefits, destinations (villas), offers, about us, contact, newsletter, social media, blog, look at the attachment, even if it is in German. The idea is that I can easily add new pages, if necessary, with the design you make. Later on we want to add a reservation system, so you can book your villa through the internet. Besides, there is a concierge service available, which organizes everything for the customer, owner, from villa to restaurant, limo service, ... & benefits and emotions through nice pictures / videos, they should be convinced to invest.

Target Market(s)

Investors (golfer and non-golfer) which have 300'000 to invest in a kind of real-estate investing club

Number of Pages Required

5+ page

Font styles to use
Sans Serif

Requirements
Must have
• It must be for wordpress, must have an exclusive touch, high quality, with nice pictures of golf courses. The Logo is gold so it has to match with gold, the font is segan or segoe semilight or similar, sans serif
Nice to have
• may be as well as the possibility to include videos of the different destinations and houses

```html
<!DOCTYPE html>
<html lang="en">
<head>
<meta charset="utf-8">
<title>Brisk Lantern Estates</title>
<link rel="stylesheet" href="https://fonts.googleapis.com/css2?family=Poppins:wght@400;500;600&family=Open+Sans:wght@400;600&display=swap">
<style>
:root{
  --gold:#e3a21a;
  --gold-deep:#c98a12;
  --ink:#1d1d1d;
  --text:#555;
  --muted:#777;
  --light:#f1f1f1;
  --footer:#111;
  --white:#fff;
}
*{margin:0;padding:0;box-sizing:border-box}
html,body{width:1200px;height:4110px;overflow:hidden;background:var(--white)}
body{position:relative;font-family:"Open Sans",Arial,sans-serif;color:var(--text)}
.abs{position:absolute}
.heading{font-family:"Poppins",Arial,sans-serif;color:var(--ink);font-weight:500}
.btn{position:absolute;background:var(--gold);color:var(--white);font-family:"Poppins",Arial,sans-serif;font-size:17px;display:flex;align-items:center;justify-content:center}
/* top bar */
.topbar{left:0;top:0;width:1200px;height:38px;background:var(--gold);color:var(--white);font-size:13px}
.topbar .contact{left:92px;top:10px;display:flex;gap:24px}
.topbar .social{right:90px;top:9px;display:flex;gap:12px}
.topbar .social span{width:20px;height:20px;background:var(--white);border-radius:3px;display:block}
/* nav */
.nav{left:0;top:38px;width:1200px;height:104px;background:var(--white)}
.brand{font-family:"Poppins",Arial,sans-serif;color:var(--gold);font-weight:500;display:flex;align-items:center;gap:10px}
.nav .brand{left:88px;top:36px;font-size:19px}
.brand i{display:block;width:14px;height:14px;background:var(--gold)}
.menu{right:90px;top:44px;display:flex;gap:48px;font-family:"Poppins",Arial,sans-serif;font-size:17px;color:#444}
.menu .active{color:var(--gold)}
/* hero */
.hero{left:0;top:142px;width:1200px;height:502px;background:linear-gradient(180deg,#7fa8c6 0%,#b9cbd6 40%,#8d8b86 70%,#5d5852 100%)}
.hero h1{position:absolute;left:0;width:1200px;top:100px;text-align:center;color:var(--white);font-family:"Poppins",Arial,sans-serif;font-weight:500;font-size:54px;letter-spacing:1px}
.hero h2{position:absolute;left:0;width:1200px;top:180px;text-align:center;color:var(--white);font-family:"Poppins",Arial,sans-serif;font-weight:400;font-size:44px}
/* about */
.about-frame{left:96px;top:762px;width:440px;height:304px;border:2px solid var(--gold)}
.about-media{left:123px;top:789px;width:440px;height:302px;background:linear-gradient(180deg,#6aa6d8,#5fa06b 55%,#2f8fb3)}
.play{left:306px;top:902px}
.about-kicker{left:603px;top:788px;color:var(--gold);font-family:"Poppins",Arial,sans-serif;font-size:22px}
.about-title{left:603px;top:818px;font-size:40px}
.about-text{left:603px;top:884px;width:505px;font-size:14px;line-height:27px}
/* benefits */
.benefits{left:0;top:1214px;width:1200px;height:636px;background:linear-gradient(180deg,#d9960f,#c9860c)}
.benefits h3{position:absolute;left:0;width:1200px;top:90px;text-align:center;color:var(--white);font-family:"Poppins",Arial,sans-serif;font-weight:500;font-size:42px}
.card{top:203px;width:315px;height:318px;background:var(--white);text-align:center;box-shadow:0 4px 14px rgba(0,0,0,.2)}
.card.dark{background:#0c0c0c}
.card .icon{width:96px;height:88px;margin:40px auto 0;background:#f4d49a;border-radius:10px}
.card.dark .icon{background:#3a3a3a}
.card h4{font-family:"Poppins",Arial,sans-serif;font-weight:500;font-size:22px;color:var(--ink);margin-top:18px}
.card.dark h4,.card.dark p{color:var(--white)}
.card p{font-size:13px;line-height:24px;margin:12px 30px 0;color:#444}
/* lists */
.section-title{font-size:42px}
.points{list-style:none;font-size:14px;line-height:24px;color:#444}
.points li{position:relative;padding-left:32px;margin-bottom:20px}
.points li::before{content:"";position:absolute;left:0;top:4px;width:16px;height:16px;border-radius:50%;background:var(--gold)}
.points li::after{content:"";position:absolute;left:4px;top:9px;width:5px;height:5px;border-top:2px solid var(--white);border-right:2px solid var(--white);transform:rotate(45deg)}
.photo{box-shadow:0 4px 14px rgba(0,0,0,.25)}
/* blog */
.blog{left:0;top:3060px;width:1200px;height:620px;background:var(--light)}
.post{top:180px;width:315px}
.post .thumb{width:315px;height:205px;box-shadow:0 3px 10px rgba(0,0,0,.2)}
.post .date{font-size:13px;margin-top:32px;color:#444}
.post h5{font-family:"Poppins",Arial,sans-serif;font-weight:400;font-size:20px;color:var(--ink);margin-top:6px}
.post p{font-size:13px;line-height:21px;margin-top:6px;color:#555}
/* footer */
.footer{left:0;top:3680px;width:1200px;height:430px;background:var(--footer);color:#ddd}
.footer h6{position:absolute;font-family:"Poppins",Arial,sans-serif;font-weight:500;font-size:18px;color:var(--white)}
.footer .brand{left:90px;top:178px;font-size:17px}
.links{left:372px;top:140px;list-style:none;font-size:13px;line-height:24px}
.links li::before{content:"›";margin-right:12px}
.info{left:581px;top:136px;font-size:13px;line-height:22px}
.info div{display:flex;gap:22px;margin-bottom:22px}
.info svg{flex:none;margin-top:3px}
.field{left:858px;width:254px;height:37px;background:var(--white);color:#666;font-size:14px;padding:9px 14px}
.copyright{left:0;top:372px;width:1200px;text-align:center;font-size:13px}
</style>
</head>
<body>

<header>
  <div class="abs topbar">
    <div class="abs contact"><span>☎ +41 44 000 12 34</span><span>✉ hello@brisklantern.example</span></div>
    <div class="abs social"><span></span><span></span><span></span><span></span></div>
  </div>
  <nav class="abs nav">
    <div class="abs brand"><i></i>BRISK LANTERN ESTATES</div>
    <div class="abs menu"><span class="active">Home</span><span>About us</span><span>Idea</span><span>Benefits</span><span>offers</span><span>Blogs</span><span>Contact Us</span></div>
  </nav>
</header>

<section class="abs hero" role="img" aria-label="Bright villa lounge with sofas opening onto a sea view">
  <h1>BRISK LANTERN ESTATES</h1>
  <h2>Villas &amp; Apartments</h2>
  <div class="btn" style="left:508px;top:276px;width:184px;height:56px;font-size:24px">View More</div>
</section>

<section class="about">
  <div class="abs about-frame"></div>
  <div class="abs about-media" role="img" aria-label="Resort pool with palm trees and sun loungers"></div>
  <svg class="abs play" width="76" height="76" viewBox="0 0 76 76"><circle cx="38" cy="38" r="34" fill="none" stroke="#fff" stroke-width="4"/><path d="M30 24 L54 38 L30 52Z" fill="#fff"/></svg>
  <div class="abs about-kicker">About</div>
  <h2 class="abs heading about-title">Brisk Lantern Estates</h2>
  <p class="abs about-text">The point of using Lorem Ipsum is that it has a more-or-less normal distribution of letters, as opposed to using 'Content here, content here', making it look like readable English. Many desktop publishing packages and web page editors now use Lorem Ipsum as their default model text, and a search for 'lorem ipsum' will uncover many web sites still in their infancy.</p>
  <div class="btn" style="left:606px;top:1042px;width:130px;height:36px">Read More</div>
</section>

<section class="abs benefits">
  <h3>Benefits</h3>
  <div class="abs card" style="left:96px"><div class="icon" role="img" aria-label="Emotional icon"></div><h4>Emotional</h4><p>They are co-owners of exclusive real estate in Top resorts, in beautiful, well-kept and safer Surroundings</p></div>
  <div class="abs card dark" style="left:449px"><div class="icon" role="img" aria-label="Practical icon"></div><h4>Practical</h4><p>You own real estate without worrying about the Take care of purchasing, administration and maintenance to have</p></div>
  <div class="abs card" style="left:792px"><div class="icon" role="img" aria-label="Monetary icon"></div><h4>Monetary</h4><p>You will be with one relatively low investment Co-owner of several, more exclusive real estate</p></div>
</section>

<section class="idea">
  <h2 class="abs heading section-title" style="left:92px;top:1980px">Our Idea</h2>
  <ul class="abs points" style="left:94px;top:2050px;width:560px">
    <li>We bring real estate investment, golf &amp; lifestyle together</li>
    <li>The idea follows a need for holidays, variety and enjoyment at the highest Level and at attractive conditions</li>
    <li>The concept is based on many discussions and is made with the help of various experts developed in various fields been</li>
    <li>Real estate in golf resorts will be from Golfers appreciated as non-golfers: the Reasons for this are:</li>
  </ul>
  <div class="btn" style="left:96px;top:2322px;width:112px;height:32px;font-size:15px">Read More</div>
  <div class="abs photo" style="left:682px;top:1984px;width:425px;height:386px;background:linear-gradient(180deg,#c9d6df,#9b8a78 70%,#7a6552)" role="img" aria-label="Terrace view with portraits of the two founders"></div>
</section>

<section class="offer">
  <div class="abs photo" style="left:93px;top:2545px;width:427px;height:384px;background:linear-gradient(180deg,#2a2620,#5a4630 55%,#1f7d8d 80%,#2a2620)" role="img" aria-label="Illuminated resort courtyard with pool at night"></div>
  <h2 class="abs heading section-title" style="left:562px;top:2545px">Our Offer</h2>
  <ul class="abs points" style="left:566px;top:2616px;width:548px">
    <li>We offer individuals and companies Fund shares of the Brisk Lantern Estates.</li>
    <li>With these you become a co-owner of one globally dispersed portfolios of exclusive and stylish villas / apartments, in World Class golf resorts.</li>
    <li>You can in this, with family and Friends, some unforgettable Enjoy holiday weeks, play golf and Take advantage of resort offers / services.</li>
    <li>We rent the remaining weeks best possible in the market, to a maximum achievable prices, which you in turn too Good is coming.</li>
  </ul>
  <div class="btn" style="left:566px;top:2880px;width:114px;height:32px;font-size:15px">Learn More</div>
</section>

<section class="abs blog">
  <h2 class="heading" style="position:absolute;left:0;width:1200px;top:70px;text-align:center;font-size:42px">Latest Blog</h2>
  <article class="abs post" style="left:90px"><div class="thumb" style="background:linear-gradient(180deg,#4a6f8a,#8a6a4a 60%,#2e8ca6)" role="img" aria-label="Resort pool at dusk"></div><div class="date">12 NOV 2018</div><h5>Neque porro quisquam</h5><p>It is a long established fact that a reader will be distracted by the readable content</p></article>
  <article class="abs post" style="left:438px"><div class="thumb" style="background:linear-gradient(180deg,#8fc0e6,#e6e2d8 55%,#3fa7c7)" role="img" aria-label="White apartment buildings above a pool"></div><div class="date">12 NOV 2018</div><h5>Dolorem ipsum quia</h5><p>It is a long established fact that a reader will be distracted by the readable content</p></article>
  <article class="abs post" style="left:786px"><div class="thumb" style="background:linear-gradient(180deg,#4f7a3c,#7aa352 50%,#3f6a2e)" role="img" aria-label="Aerial view of a golf course"></div><div class="date">12 NOV 2018</div><h5>Porro quisquam est qui</h5><p>It is a long established fact that a reader will be distracted by the readable content</p></article>
</section>

<footer class="abs footer">
  <div class="abs brand"><i></i>BRISK LANTERN ESTATES</div>
  <h6 style="left:364px;top:82px">QUICK LINKS</h6>
  <ul class="abs links"><li>Home</li><li>About us</li><li>Product</li><li>Services</li><li>Contact Us</li></ul>
  <h6 style="left:581px;top:82px">CONTACT US</h6>
  <div class="abs info">
    <div><svg width="14" height="18" viewBox="0 0 14 18"><path d="M7 0a7 7 0 0 1 7 7c0 5-7 11-7 11S0 12 0 7a7 7 0 0 1 7-7z" fill="#fff"/><circle cx="7" cy="7" r="2.5" fill="#111"/></svg><span>12, Ember Row, Westfield,<br>WA 6000</span></div>
    <div><svg width="14" height="14" viewBox="0 0 14 14"><path d="M3 0l3 3-2 2c1 2 3 4 5 5l2-2 3 3-2 3C6 14 0 8 0 2z" fill="#fff"/></svg><span>08 5550 1400</span></div>
    <div><svg width="15" height="11" viewBox="0 0 15 11"><rect width="15" height="11" fill="#fff"/><path d="M0 0l7.5 6L15 0" fill="none" stroke="#111" stroke-width="1.5"/></svg><span>info@brisklantern.example</span></div>
  </div>
  <h6 style="left:858px;top:82px">NEWSLETTER</h6>
  <div class="abs field" style="top:140px">Your Name</div>
  <div class="abs field" style="top:203px">Email address</div>
  <div class="btn" style="left:858px;top:255px;width:120px;height:37px">SEND</div>
  <div class="abs copyright">© Copyright 2018 . All Rights Reserved.</div>
</footer>

</body>
</html>
```